Industrial Project Sign

We need an eye catching (but professional) industrial project sign that will be very large (roughly 12' high x 18' wide). This sign will be highly visible from the adjacent high speed highway.

* The following needs to be at the bottom of the signage: Logo (uploaded), Name (Pillar Ventures Group, Inc.) (uploaded) and phone number (555)613-8874

*Name of Project - "Brambleford Industrial Center"

* Text items
Land for Sale
Build to Suit
Zoning: Industrial (G I & L I)

* Interesting background that is eye catching
Updates

Good morning all,

We are considering all designers options as we go and are waiting for the final designs to come in by the 4th so that we can give each one a good look.   If you have any new designs, questions, further design options or any tweeks you want to do to current designs, please do so at this time.

Thanks to all of you for your submissions.

Industry/Entity Type

Industrial

```html
<!DOCTYPE html>
<html lang="en">
<head>
<meta charset="utf-8">
<title>Brambleford Industrial Center – Project Sign</title>
<link rel="stylesheet" href="https://fonts.googleapis.com/css2?family=Poiret+One&family=Roboto+Condensed:wght@400&family=Montserrat:wght@600&family=Open+Sans:wght@400&display=swap">
<style>
  :root {
    --sign-white: #ffffff;
    --ink-black: #000000;
    --band-black: #000000;
    --band-red: #8e0f0a;
    --brand-red: #7d1a16;
    --brand-grey: #555555;
  }
  html, body {
    margin: 0;
    padding: 0;
    overflow: hidden;
    background: var(--sign-white);
  }
  .sign {
    position: relative;
    width: 1200px;
    height: 761px;
    background: var(--sign-white);
    overflow: hidden;
  }
  .project-name {
    position: absolute;
    top: 0;
    left: 0;
    width: 100%;
    margin: 0;
    text-align: center;
    font-family: "Poiret One", cursive;
    font-weight: 400;
    font-size: 72px;
    line-height: 84px;
    letter-spacing: 3px;
    color: var(--ink-black);
    white-space: nowrap;
  }
  .offer-band {
    position: absolute;
    top: 105px;
    left: 0;
    width: 100%;
    height: 131px;
    background: var(--band-black);
    display: flex;
    align-items: center;
    justify-content: center;
  }
  .offer-text {
    margin: 0;
    font-family: "Roboto Condensed", sans-serif;
    font-weight: 400;
    font-size: 92px;
    line-height: 1;
    color: var(--sign-white);
    white-space: nowrap;
    letter-spacing: -2px;
  }
  .zoning {
    position: absolute;
    top: 294px;
    left: 0;
    width: 100%;
    margin: 0;
    text-align: center;
    font-family: "Open Sans", sans-serif;
    font-weight: 400;
    font-size: 88px;
    line-height: 110px;
    color: var(--ink-black);
    white-space: nowrap;
    letter-spacing: -2px;
  }
  .phone-band {
    position: absolute;
    top: 437px;
    left: 0;
    width: 100%;
    height: 115px;
    background: var(--band-red);
    display: flex;
    align-items: center;
    justify-content: center;
  }
  .phone {
    font-family: "Montserrat", sans-serif;
    font-weight: 600;
    font-size: 86px;
    line-height: 1;
    color: var(--sign-white);
    letter-spacing: 7px;
    white-space: nowrap;
  }
  .developer {
    position: absolute;
    top: 590px;
    left: 0;
    width: 100%;
    height: 150px;
    display: flex;
    align-items: center;
    justify-content: center;
    gap: 60px;
  }
  .developer-mark {
    width: 110px;
    height: 110px;
    background: var(--brand-red);
  }
  .developer-name {
    font-family: "Open Sans", sans-serif;
    font-weight: 400;
    font-size: 27px;
    color: var(--brand-grey);
    white-space: nowrap;
  }
</style>
</head>
<body>
  <main class="sign">
    <h1 class="project-name">Brambleford Industrial Center</h1>

    <div class="offer-band">
      <p class="offer-text">LAND FOR SALE•BUILD TO SUIT</p>
    </div>

    <p class="zoning">ZONED INDUSTRIAL GI &amp; LI</p>

    <div class="phone-band">
      <span class="phone">555-613-8874</span>
    </div>

    <div class="developer">
      <span class="developer-mark" aria-hidden="true"></span>
      <span class="developer-name">Pillar Ventures Group, Inc.</span>
    </div>
  </main>
</body>
</html>
```